Thornwell Building Company - advertisement poster

I am looking to print some canvas signs to advertise my general contracting company, Thornwell Building Company. The sign will measure 6' long x 3' high so the size should match that ratio. I already have a logo icon, which is the Letter 'A' and some trees that I would like to incorporate, see attached. I would also like the to have the following information listed:
1) phone number: 472-318-6095
2) email: thornwellbuildingcompany@mailvistra.net
3) website: thornwellbuildingcompany.com
4) Lic#5386204
5) I want to use this text: "BUILD WITH THE T-CREW!"

The ad should be relatively simple and clean. Black and Green are my company colors. I am open to creative ideas!

Target Market(s)

People looking to renovate their homes

Industry/Entity Type

Construction

Colors
59FF00
82FF00
B8FF75
E3FFCB
F4FFEA

Requirements
Must have
• Must have my company logo
Should not have
• No photos or complex graphics

```html
<!DOCTYPE html>
<html lang="en">
<head>
<meta charset="utf-8">
<title>Thornwell Building Company – Sign</title>
<link rel="stylesheet" href="https://fonts.googleapis.com/css2?family=Oswald:wght@400;600&family=Michroma&display=swap">
<style>
  :root {
    --backdrop: #2e2f47;
    --navy: #363469;
    --green: #76b650;
    --green-soft: #9fcf82;
    --white: #ffffff;
  }
  * { margin: 0; padding: 0; box-sizing: border-box; }
  html, body {
    width: 1200px;
    height: 722px;
    overflow: hidden;
    background: var(--backdrop);
  }
  .sign {
    position: absolute;
    left: 129.5px;
    top: 125.5px;
    width: 940.5px;
    height: 470px;
    display: block;
    background: var(--white);
  }
  .band--top { fill: var(--green); }
  .band--bottom { fill: var(--navy); }
  .line-green { stroke: var(--green); stroke-width: 2; }

  .brand-name,
  .headline,
  .phone,
  .license,
  .email,
  .website { font-family: "Oswald", sans-serif; }

  .brand-name { font-weight: 600; fill: var(--navy); }
  .brand-name__main { font-size: 56px; }
  .brand-name__sub { font-size: 24px; }

  .brand-phone,
  .tagline { font-family: "Michroma", sans-serif; fill: var(--navy); }
  .brand-phone { font-size: 19px; }
  .tagline { font-size: 23px; }

  .headline { font-size: 65px; font-weight: 600; fill: var(--navy); }
  .headline__accent { fill: var(--green); }

  .phone { font-size: 64px; font-weight: 600; fill: var(--navy); }
  .email { font-size: 24px; font-weight: 400; fill: var(--green); }
  .website { font-size: 31px; font-weight: 400; fill: var(--navy); }
  .license { font-size: 66px; font-weight: 600; fill: var(--navy); }

  .icon-disc--navy { fill: var(--navy); }
  .icon-disc--green { fill: var(--green); }
  .icon-glyph { fill: none; stroke: var(--white); stroke-width: 1.6; }
  .icon-glyph--solid { fill: var(--white); stroke: none; }
</style>
</head>
<body>
  <svg class="sign" viewBox="0 0 940.5 470" width="940.5" height="470">
    <!-- corner bands -->
    <polygon class="band--top" points="0,0 500.5,0 485,19 0,19"/>
    <polygon class="band--bottom" points="439,451 940.5,451 940.5,470 455,470"/>

    <!-- brand block -->
    <g class="brand">
      <defs>
        <linearGradient id="emblem-fill" x1="0" y1="0" x2="1" y2="1">
          <stop offset="0" stop-color="#76b650"/>
          <stop offset="1" stop-color="#363469"/>
        </linearGradient>
      </defs>
      <rect class="brand-emblem" x="155" y="77" width="208" height="148" rx="4"
            fill="url(#emblem-fill)" opacity="0.85"
            role="img" aria-label="Company logo emblem: house with trees and mountains"/>
      <text class="brand-name brand-name__main" x="31" y="282" textLength="453" lengthAdjust="spacingAndGlyphs">THORNWELL</text>
      <text class="brand-name brand-name__sub" x="34" y="313" textLength="451" lengthAdjust="spacing">BUILDING COMPANY</text>
      <text class="brand-phone" x="143" y="340.5" textLength="232" lengthAdjust="spacingAndGlyphs">472.318.6095</text>
      <text class="tagline" x="100.5" y="424.5" textLength="316" lengthAdjust="spacingAndGlyphs">JOIN THE T-CREW!</text>
    </g>

    <!-- headline -->
    <text class="headline" x="364.5" y="129.5" textLength="545" lengthAdjust="spacingAndGlyphs">BUILD <tspan class="headline__accent">WITH THE</tspan> T-CREW!</text>

    <!-- divider and rule -->
    <line class="line-green" x1="519" y1="158" x2="519" y2="389.5"/>
    <line class="line-green" x1="448" y1="415" x2="910.5" y2="415"/>

    <!-- phone -->
    <g class="contact contact--phone">
      <circle class="icon-disc--navy" cx="569" cy="192" r="18"/>
      <path class="icon-glyph--solid" transform="translate(551 174)"
            d="M12.5 9.5c1-.8 2-.6 2.6.3l1.6 2.6c.5.8.3 1.7-.4 2.3l-1 .8c.8 2 2.4 3.7 4.3 4.6l.9-1c.6-.7 1.6-.8 2.3-.3l2.6 1.7c.9.6 1 1.7.2 2.6l-1.2 1.3c-1 1-2.6 1.3-4 .6-4.2-2-7.4-5.4-9.1-9.8-.5-1.4 0-2.9 1.2-3.9z"/>
      <text class="phone" x="603.5" y="217" textLength="300" lengthAdjust="spacingAndGlyphs">472-318-6095</text>
    </g>

    <!-- email -->
    <g class="contact contact--email">
      <circle class="icon-disc--green" cx="569" cy="248.5" r="18"/>
      <g transform="translate(551 230.5)">
        <rect class="icon-glyph" x="8" y="11.5" width="20" height="13" rx="1"/>
        <polyline class="icon-glyph" points="8.5,12.5 18,19.5 27.5,12.5"/>
      </g>
      <text class="email" x="603.5" y="257" textLength="305" lengthAdjust="spacingAndGlyphs">thornwellbuildingcompany@mailvistra.net</text>
    </g>

    <!-- website -->
    <g class="contact contact--web">
      <circle class="icon-disc--navy" cx="569" cy="298.5" r="18"/>
      <g class="icon-glyph" transform="translate(551 280.5)" stroke-width="1.4">
        <circle cx="18" cy="18" r="9"/>
        <ellipse cx="18" cy="18" rx="4" ry="9"/>
        <line x1="18" y1="9" x2="18" y2="27"/>
        <line x1="9" y1="18" x2="27" y2="18"/>
        <line x1="10.5" y1="13.5" x2="25.5" y2="13.5"/>
        <line x1="10.5" y1="22.5" x2="25.5" y2="22.5"/>
      </g>
      <text class="website" x="603.5" y="303" textLength="306" lengthAdjust="spacingAndGlyphs">thornwellbuildingcompany.com</text>
    </g>

    <!-- license -->
    <text class="license" x="600.5" y="384.5" textLength="299" lengthAdjust="spacingAndGlyphs">Lic#5386204</text>
  </svg>
</body>
</html>
```